Coral Beacon Stationery Design Project

I am looking for a suitable stationary design for my company Coral Beacon Pty Ltd (ACN 582 914 306).

The requirements can be better explained by visiting my website
"coral-beacon-trust.org"

I will be sending letters to Ministers of State and the Heads of Government Agencies so the theme needs to be formal and serious.

A theme with a shield or similar picking on the "guardian" concept would be appropriate

Target Market(s)

Ministers of State and Department Agency Heads and legal firms, the heads of Trustee Companies as well as Members of Coral Beacon

Industry/Entity Type

Government

Requirements
Must have
• Letterhead design is a priority - Business Card secondary

Must include tag line "Steady hands for every estate we tend" with a registered trade mark superscript at the end that is an R in a circle {Windows Alt +0174 on numeric keypad or Mac Option +R}.

Must include website address "Coral-Beacon-Trust.org" plus Email address "corbeacon@mailvessel.net

Company name "Coral Beacon Pty. Ltd." and Australian Company Number "ACN 582 914 306" needs to be shown more discretely

Address is "47 Finch Crescent, Marrowdale, 3291"
Nice to have
• A watermark is something to be considered

```html
<!DOCTYPE html>
<html lang="en">
<head>
<meta charset="utf-8">
<title>Coral Beacon Stationery</title>
<link href="https://fonts.googleapis.com/css2?family=Arimo:wght@400;700&display=swap" rel="stylesheet">
<style>
  :root {
    --backdrop: #f1f1f2;
    --paper: #ffffff;
    --navy: #0f2a4e;
    --navy-deep: #0a1f3d;
    --royal: #1763a8;
    --sky: #2b86cf;
    --gold: #c89a4a;
    --ink: #1a1a1a;
    --rule: #e6c9c9;
    --watermark: #f3f3f4;
  }
  * { margin: 0; padding: 0; box-sizing: border-box; }
  html, body {
    width: 1200px; height: 1112px; overflow: hidden;
    background: radial-gradient(ellipse at 60% 40%, #fafafa 0%, var(--backdrop) 75%);
    font-family: "Arimo", Arial, sans-serif;
    color: var(--ink);
  }
  .stage { position: relative; width: 1200px; height: 1112px; }

  /* Letterhead */
  .letterhead {
    position: absolute; left: 70px; top: 70px; width: 688px; height: 973px;
    background: var(--paper); box-shadow: 0 1px 3px rgba(0,0,0,.12); overflow: hidden;
  }
  .watermark {
    position: absolute; left: 251px; top: 370px; width: 386px; height: 386px;
    background: var(--watermark);
  }
  .brand { display: flex; align-items: center; gap: 10px; }
  .brand-mark { width: 44px; height: 44px; background: var(--navy); flex: none; }
  .brand-name {
    font-weight: 700; color: var(--navy); font-size: 29px; line-height: 28px; letter-spacing: -0.5px;
  }
  .letterhead .brand { position: absolute; left: 33px; top: 35px; }
  .letterhead .divider {
    position: absolute; left: 457px; top: 36px; width: 1px; height: 107px;
    background: linear-gradient(var(--paper), var(--rule), var(--paper));
  }
  .contact-block {
    position: absolute; right: 28px; top: 26px; text-align: right;
    font-size: 11.5px; line-height: 14px;
  }
  .contact-block .company { font-weight: 700; margin-bottom: 13px; }
  .contact-block p + p { margin-top: 10px; }
  .contact-block b { font-weight: 700; }
  .tagline {
    position: absolute; left: 18px; top: 882px; width: 190px; text-align: center;
    color: var(--navy); font-weight: 700; font-size: 16.5px; line-height: 20px; letter-spacing: -0.3px;
  }
  .tagline sup { font-size: 9px; line-height: 0; vertical-align: 6px; margin-left: 1px; }
  .swoosh { position: absolute; left: 0; bottom: 0; display: block; }

  /* Business cards */
  .card {
    position: absolute; left: 823px; width: 296px; height: 180px;
    box-shadow: 0 1px 3px rgba(0,0,0,.15); overflow: hidden;
  }
  .card-front { top: 132px; background: var(--paper); }
  .card-back { top: 323px; background: linear-gradient(135deg, #10305a, var(--navy-deep)); }
  .card-details {
    position: absolute; left: 16px; top: 31px; font-size: 7.3px; line-height: 9px;
  }
  .card-details .company { font-weight: 700; margin-bottom: 7px; }
  .card-details p + p { margin-top: 6px; }
  .card-front .brand { position: absolute; left: 150px; top: 40px; gap: 6px; }
  .card .brand-mark { width: 24px; height: 24px; }
  .card .brand-name { font-size: 17px; line-height: 17px; letter-spacing: -0.3px; }
  .holder {
    position: absolute; left: 145px; top: 100px; width: 150px; text-align: center;
    font-weight: 700; font-size: 11px;
  }
  .card-back .brand { position: absolute; left: 72px; top: 62px; gap: 8px; }
  .card-back .brand-mark { width: 32px; height: 32px; background: var(--gold); }
  .card-back .brand-name { color: #ffffff; font-size: 21px; line-height: 21px; }
  .card-back .web {
    position: absolute; left: 0; right: 0; top: 163px; text-align: center;
    color: #ffffff; font-size: 7.5px;
  }
</style>
</head>
<body>
<div class="stage">

  <section class="letterhead">
    <div class="watermark" role="img" aria-label="Faint brand watermark"></div>
    <div class="brand">
      <span class="brand-mark"></span>
      <span class="brand-name">Coral<br>Beacon</span>
    </div>
    <span class="divider"></span>
    <div class="contact-block">
      <p class="company">Coral Beacon Pty. Ltd.</p>
      <p>ACN 582 914 306<br>47 Finch Crescent, Marrowdale, 3291</p>
      <p><b>Phone</b> 5487 60291<br><b>Fax</b> 5487 60292</p>
      <p><b>Email</b> corbeacon@mailvessel.net<br>www.Coral-Beacon-Trust.org</p>
    </div>
    <p class="tagline">Steady hands for every estate we tend<sup>®</sup></p>
    <svg class="swoosh" width="688" height="160" viewBox="0 0 688 160" aria-hidden="true">
      <path d="M0,133 Q360,128 688,0 L688,160 L0,160 Z" fill="var(--gold)"/>
      <path d="M0,141 Q360,138 688,22 L688,160 L0,160 Z" fill="var(--navy)"/>
      <path d="M0,146 Q380,144 688,52 L688,66 Q380,152 0,152 Z" fill="var(--royal)"/>
      <path d="M0,150 Q400,150 688,70 L688,78 Q400,156 0,155 Z" fill="var(--sky)"/>
      <path d="M0,154 Q420,156 688,86 L688,160 L0,160 Z" fill="var(--navy-deep)"/>
    </svg>
  </section>

  <section class="card card-front">
    <div class="card-details">
      <p class="company">Coral Beacon Pty. Ltd.</p>
      <p>ACN 582 914 306<br>47 Finch Crescent, Marrowdale, 3291</p>
      <p><b>Mobile</b> 0418 73 552<br><b>Phone</b> 5487 60291<br><b>Fax</b> 5487 60292</p>
      <p><b>Email</b> corbeacon@mailvessel.net<br>www.Coral-Beacon-Trust.org</p>
    </div>
    <div class="brand">
      <span class="brand-mark"></span>
      <span class="brand-name">Coral<br>Beacon</span>
    </div>
    <p class="holder">Owen Hartley</p>
    <svg class="swoosh" width="296" height="50" viewBox="0 0 296 50" aria-hidden="true">
      <path d="M0,38 Q160,36 296,0 L296,50 L0,50 Z" fill="var(--gold)"/>
      <path d="M0,41 Q160,40 296,5 L296,50 L0,50 Z" fill="var(--navy)"/>
      <path d="M0,44 Q170,44 296,14 L296,19 Q170,47 0,46 Z" fill="var(--sky)"/>
      <path d="M0,47 Q180,48 296,22 L296,50 L0,50 Z" fill="var(--navy-deep)"/>
    </svg>
  </section>

  <section class="card card-back">
    <div class="brand">
      <span class="brand-mark"></span>
      <span class="brand-name">Coral<br>Beacon</span>
    </div>
    <p class="web">www.Coral-Beacon-Trust.org</p>
  </section>

</div>
</body>
</html>
```